Harlune Painting

Need business card design

Target Market(s)

Paint

Industry/Entity Type

Painting

Requirements
Must have
• Brice Halvorn | Superviser
| HarLune Painting
| mobile: (360) 555-0148
| email: Brice@harluneinc.example
| site: www.harluneinc.example
| address: 718 Corliss Rd NE Ste 300, Olympia, WA 98501

```html
<!DOCTYPE html>
<html lang="en">
<head>
<meta charset="utf-8">
<title>Harlune Painting – Business Card</title>
<link href="https://fonts.googleapis.com/css2?family=Montserrat:wght@400;500;600;700&display=swap" rel="stylesheet">
<style>
  :root {
    --navy: #213f85;
    --blue: #2a6fc0;
    --green: #5cb83c;
    --grey-text: #5a5f66;
    --paper: #ffffff;
    --stage: #e6e7e9;
  }
  * { box-sizing: border-box; margin: 0; padding: 0; }
  html, body {
    width: 1200px; height: 913px; overflow: hidden;
    background: var(--stage);
    font-family: "Montserrat", sans-serif;
  }
  .canvas { position: relative; width: 1200px; height: 913px; }

  .card {
    position: absolute;
    width: 560px; height: 320px;
    box-shadow: 0 6px 18px rgba(0,0,0,0.18);
    overflow: hidden;
  }
  .card--back { left: 80px; top: 90px; background: var(--navy); }
  .card--front { left: 560px; top: 500px; background: var(--paper); }

  .brand {
    position: absolute;
    display: flex; align-items: center; gap: 10px;
    font-weight: 700; letter-spacing: 1px; text-transform: uppercase;
    white-space: nowrap;
  }
  .brand__dot { width: 18px; height: 18px; border-radius: 50%; flex: none; }
  .card--back .brand {
    left: 0; right: 0; top: 0; bottom: 0; justify-content: center;
    font-size: 34px; color: var(--paper);
  }
  .card--back .brand__dot { background: var(--paper); }
  .card--front .brand {
    left: 26px; top: 150px; font-size: 17px; letter-spacing: 0.5px; color: var(--navy);
  }
  .card--front .brand__dot { background: var(--navy); width: 12px; height: 12px; }

  .divider {
    position: absolute; left: 282px; top: 48px;
    width: 2px; height: 150px; background: var(--green);
  }
  .contact { position: absolute; left: 300px; top: 40px; color: var(--grey-text); }
  .contact__name { font-size: 19px; font-weight: 700; letter-spacing: 0.5px; white-space: nowrap; }
  .contact__first { color: var(--blue); }
  .contact__last { color: var(--green); }
  .contact__title { font-size: 10px; letter-spacing: 1px; margin-top: 1px; }
  .contact__address { font-size: 11.5px; line-height: 16px; margin-top: 12px; }
  .contact__list { list-style: none; margin-top: 6px; font-size: 11.5px; }
  .contact__list li { display: flex; align-items: center; gap: 8px; height: 18px; white-space: nowrap; }
  .contact__list svg { width: 12px; height: 12px; fill: var(--navy); flex: none; }

  .card__band { position: absolute; left: 0; bottom: 0; width: 560px; height: 320px; }
</style>
</head>
<body>
<div class="canvas">

  <section class="card card--back" aria-label="Card back">
    <div class="brand"><span class="brand__dot"></span>Harlune Painting</div>
  </section>

  <section class="card card--front" aria-label="Card front">
    <svg class="card__band" viewBox="0 0 560 320" aria-hidden="true">
      <path d="M0 320 L0 318 C 180 304 380 256 560 190 L560 320 Z" fill="var(--navy)"/>
      <path d="M0 312 C 180 298 380 248 560 182" fill="none" stroke="var(--green)" stroke-width="4"/>
    </svg>

    <div class="brand"><span class="brand__dot"></span>Harlune Painting</div>

    <div class="divider"></div>

    <div class="contact">
      <p class="contact__name"><span class="contact__first">BRICE</span> <span class="contact__last">HALVORN</span></p>
      <p class="contact__title">SUPERVISER</p>
      <p class="contact__address">718 Corliss Rd NE Ste 300,<br>Olympia, WA 98501</p>
      <ul class="contact__list">
        <li><svg viewBox="0 0 24 24"><path d="M6.6 10.8a15 15 0 0 0 6.6 6.6l2.2-2.2a1 1 0 0 1 1-.25 11.4 11.4 0 0 0 3.6.57 1 1 0 0 1 1 1V20a1 1 0 0 1-1 1A17 17 0 0 1 3 4a1 1 0 0 1 1-1h3.5a1 1 0 0 1 1 1c0 1.25.2 2.45.57 3.57a1 1 0 0 1-.25 1z"/></svg>(360) 555-0148</li>
        <li><svg viewBox="0 0 24 24"><path d="M2 5h20v14H2z M2 5l10 8 10-8" stroke="#fff" stroke-width="1.5"/></svg>Brice@harluneinc.example</li>
        <li><svg viewBox="0 0 24 24"><circle cx="12" cy="12" r="10"/><path d="M2 12h20M12 2c3 3 3 17 0 20M12 2c-3 3-3 17 0 20" stroke="#fff" stroke-width="1.4" fill="none"/></svg>www.harluneinc.example</li>
      </ul>
    </div>
  </section>

</div>
</body>
</html>
```